Broschüre für Softwareentwickler
Zielgruppe
Softwareentwicklung für die Immobilienwirtschaft, speziell Bauträger, Projektentwickler und Generalunternehmer. TOLDA ist eine von uns - Brenner Software und Beratung AG - entwickelte Branchensoftware für die kaufmännische Abwicklung der Prozesse in der Immobilienwirtschaft.
Aufgabenstellung
Wir wollen unseren aktuellen Flyer/Broschüre für unsere Software TOLDA überarbeiten lassen. Es soll weiterhin/quer in der Mitte gefaltet sein - 4-seiter - sein. Das Firmenlogo wurde zwischenzeitlich geändert und finden Sie im Anhang. Das Logo für die Software TOLDA soll so erhalten bleiben (finden Sie ebenfalls im Anhang).
Beide Logos sollen farbunabhängig sein und auch als Outline sowie invertiert abgebildet werden können. Das Logo-Blau vom Produktlogo TOLDA muss nicht erhalten bleiben, wir möchten eher weg von Blau.
Das aktuell im Flyer enthaltenen Bilder sollen verändert/nicht mehr genutzt werden. Das Layout der Broschüre soll angepasst werden. Wir wollen hier neue Bilder/andere Bilder verwenden. Mehr in Anlehnung an die Homepage-Bilder.
Der Textumfang wird gleich bleiben, wird aber noch angepasst - kommt noch.
Die Aufteilung und die Positionen der Texte/Bilder dürfen gerne verändert werden. Wir freuen uns über kreative, ganz neue Designzusammenstellungen.

```html
<!DOCTYPE html>
<html lang="de">
<head>
<meta charset="utf-8">
<title>TOLDA – Broschüre Innenseiten</title>
<link href="https://fonts.googleapis.com/css2?family=Open+Sans:wght@400;600;700;800&display=swap" rel="stylesheet">
<style>
:root{
  --blue:#0d57a3;
  --lavender:#b7b9dc;
  --text:#3c3f45;
  --paper:#fbfbfc;
  --stage:#dedfe2;
  --rail:#8aa0c2;
  --photo-a:#5d6c86;
  --photo-b:#c9c3bb;
  --photo-c:#3f4d66;
}
*{box-sizing:border-box;margin:0;padding:0}
html,body{width:1200px;height:776px;overflow:hidden}
body{background:var(--stage);font-family:"Open Sans",Arial,sans-serif;color:var(--text);position:relative}
.spread{position:absolute;left:60px;top:28px;width:1080px;height:720px;display:flex;box-shadow:0 10px 30px rgba(0,0,0,.18)}
.page{position:relative;width:540px;height:720px;overflow:hidden}
.page--left{background:linear-gradient(90deg,var(--paper) 88%,#eceef1)}
.page--right{background:linear-gradient(90deg,#eceef1,var(--paper) 12%)}
.abs{position:absolute}

.header-band{left:0;top:0}
.header-kicker{right:30px;top:14px;color:#fff;font-size:10px;font-weight:600}
.header-title{left:28px;top:44px;color:#fff;font-size:19px;font-weight:800;line-height:1.2}
.header-text{left:28px;top:72px;width:480px;color:#fff;font-size:9.5px;line-height:1.35}

.section-title{left:32px;top:200px;color:var(--blue);font-size:19px;font-weight:800;line-height:1.2}
.intro{left:32px;top:230px;width:470px;font-size:9.5px;line-height:1.38}
.lead{left:32px;top:302px;font-size:9.5px}

.col{font-size:9.6px;line-height:1.3}
.col-a{left:32px;top:322px;width:230px}
.col-b{left:282px;top:322px;width:235px}
.label{display:inline-block;background:var(--blue);color:#fff;font-weight:700;font-size:11.5px;line-height:1.4;padding:1px 40px 1px 8px;margin:8px 0 4px}
.ticks{list-style:none}
.ticks li{position:relative;padding-left:16px;margin-bottom:1px}
.ticks li::before{content:"✓";position:absolute;left:2px;top:0;color:var(--blue);font-weight:700}

.footer-url{left:32px;bottom:18px;font-size:8px}
.page-no{right:30px;bottom:18px;font-size:7.5px}

.photo-top{left:0;top:0}
.rail{left:40px;top:218px;height:250px;border-left:1.5px dotted var(--rail)}
.rail-b{left:296px;top:218px;height:90px}
.features{font-size:9.2px;line-height:1.3}
.feat{display:flex;gap:10px;margin-bottom:11px}
.feat-title{color:var(--blue);font-weight:700;font-size:10.5px}
.feat-list{margin-top:2px}
.feat-col-a{left:28px;top:200px;width:250px}
.feat-col-b{left:284px;top:200px;width:240px}
.icon{flex:0 0 26px;width:26px;height:26px}

.photo-team{left:270px;top:472px;width:250px;height:165px;border-radius:2px;background:linear-gradient(135deg,#b9bcc2,#e6e3de 55%,#8c8f96)}
.service{left:24px;top:505px;width:290px;height:182px;background:var(--blue);color:#fff;padding:16px 20px}
.service-title{font-size:17px;font-weight:800;line-height:1.2;margin-bottom:8px}
.service .ticks{font-size:9.6px;line-height:1.35}
.service .ticks li::before{color:#fff}
</style>
</head>
<body>
<main class="spread">

  <section class="page page--left">
    <svg class="abs header-band" width="540" height="190" viewBox="0 0 540 190" aria-hidden="true">
      <path d="M0 0H540V132C470 138 420 150 370 170C340 182 300 180 260 176L0 160Z" fill="var(--lavender)"/>
      <path d="M0 0H540V118C460 124 410 138 360 158C330 170 300 170 260 166L0 150Z" fill="var(--blue)"/>
    </svg>
    <p class="abs header-kicker">Ihr Mehrwert</p>
    <h1 class="abs header-title">Optimieren Sie Ihre Prozesse</h1>
    <p class="abs header-text">TOLDA – die Bau-Software – wurde speziell für Unternehmen entwickelt, welche eine ganzheitliche Lösung für Ihre Geschäftsprozesse suchen. TOLDA deckt alle kaufmännischen Prozesse eines Bauträgers ab und bietet Schnittstellen zu den wichtigen Partnern der Branche wie BAUDAT, ImmoLink, Textra Write, Calc, Mail, Dokumentenarchiven sowie zu den gängigen Finanzbuchhaltungen.</p>

    <h2 class="abs section-title">Funktionen im Überblick</h2>
    <p class="abs intro">Von der Projektentwicklung über die Bauabwicklung bis hin zum Vertrieb und Verkauf decken wir Ihre Anforderungen an eine intuitiv zu bedienende Software ab. TOLDA lässt sich vollständig an Ihre Geschäftsprozesse anpassen. Mit verschiedenen Einstellungen sind Sie in der Lage, die Software auf Ihre Bedürfnisse einzurichten. Zudem bieten wir kundenindividuelle Anpassungen an.</p>
    <p class="abs lead">In der Basisvariante von TOLDA sind die folgenden Funktionen beinhaltet:</p>

    <div class="abs col col-a">
      <span class="label">Allgemein</span>
      <ul class="ticks">
        <li>Adressverwaltung</li>
        <li>Projektverwaltung</li>
        <li>Dokumentenarchiv</li>
        <li>Aufgabenverwaltung</li>
        <li>Beziehungen (Projektbeteiligtenliste)</li>
        <li>Dashboard</li>
        <li>Über 50 Reports/Auswertungen, auf Firmen-Design anpassbar</li>
        <li>Serienbriefe und Serienemails an Interessenten, Kunden, Handwerker etc.</li>
      </ul>
      <span class="label">Projektentwicklung</span>
      <ul class="ticks">
        <li>Grundstücksakquisen</li>
        <li>Kalkulationen</li>
      </ul>
      <span class="label">Kundenabwicklung</span>
      <ul class="ticks">
        <li>Interessentenverwaltung</li>
        <li>Reservierungslisten</li>
        <li>Kundenangebote/Bemusterungen</li>
        <li>Sonderwunschabwicklung (Mehr- und Minderleistungen)</li>
      </ul>
    </div>

    <div class="abs col col-b">
      <ul class="ticks" style="margin-top:8px">
        <li>Kundenverträge (Kauf- oder Werkverträge)</li>
        <li>Rechnungen erstellen nach Ratenplan (inkl. Serienrechnungen)</li>
        <li>Rechnungen ohne Ratenplan schreiben</li>
        <li>Zahlungen und offene Postenliste</li>
        <li>Abnahmen mit Kunden</li>
        <li>Abwicklung von Makleraufträgen</li>
      </ul>
      <span class="label" style="margin-top:18px">Bauabwicklung</span>
      <ul class="ticks">
        <li>Arbeitspakete (Bauzeitenplanung)</li>
        <li>Ausschreibung von Aufträgen</li>
        <li>Auftragsvergabe</li>
        <li>Rechnungseingangsbuch und Freigabeprozesse</li>
        <li>Zahlung von Rechnungen</li>
        <li>Kostenkontrolle</li>
        <li>Abnahmen mit Handwerkern/Gewerken</li>
        <li>Baumängelmanagement</li>
        <li>Bautenstandsberichte</li>
        <li>Leistungskatalog (Artikelstamm)</li>
      </ul>
    </div>

    <p class="abs footer-url">www.bautraeger-werkbank.de</p>
    <p class="abs page-no">01</p>
  </section>

  <section class="page page--right">
    <svg class="abs photo-top" width="540" height="180" viewBox="0 0 540 180" role="img" aria-label="Foto: Team im Büro bespricht sich gemeinsam am Laptop">
      <defs>
        <linearGradient id="teamPhoto" x1="0" y1="0" x2="1" y2="1">
          <stop offset="0" stop-color="var(--photo-a)"/>
          <stop offset=".55" stop-color="var(--photo-b)"/>
          <stop offset="1" stop-color="var(--photo-c)"/>
        </linearGradient>
      </defs>
      <path d="M260 160C300 150 360 132 420 126C470 122 510 120 540 118V132C500 134 460 138 420 144C360 152 310 166 270 176Z" fill="var(--lavender)"/>
      <path d="M0 0H540V112C480 116 420 120 360 134C320 144 290 160 250 172C200 164 120 140 0 118Z" fill="url(#teamPhoto)"/>
    </svg>

    <div class="abs rail"></div>
    <div class="abs rail rail-b"></div>

    <div class="abs features feat-col-a">
      <div class="feat">
        <svg class="icon" viewBox="0 0 26 26" aria-hidden="true"><circle cx="13" cy="13" r="12" fill="#fff" stroke="var(--blue)" stroke-width="1.5"/><circle cx="13" cy="9" r="2" fill="var(--blue)"/><path d="M10 12h6l-1 7h-4z" fill="var(--blue)"/></svg>
        <div><p class="feat-title">Benutzerfreundliche Oberfläche</p><p>Intuitiv mit TOLDA arbeiten</p></div>
      </div>
      <div class="feat">
        <svg class="icon" viewBox="0 0 26 26" aria-hidden="true"><circle cx="13" cy="13" r="12" fill="#fff" stroke="var(--blue)" stroke-width="1.5"/><rect x="7" y="8" width="12" height="8" rx="1" fill="none" stroke="var(--blue)" stroke-width="1.5"/><path d="M10 19h6M13 16v3" stroke="var(--blue)" stroke-width="1.5"/></svg>
        <div><p class="feat-title">Geräte-unabhängig</p><p>Fenix, Pomo, Robix, Tuxon</p></div>
      </div>
      <div class="feat">
        <svg class="icon" viewBox="0 0 26 26" aria-hidden="true"><circle cx="13" cy="13" r="12" fill="#fff" stroke="var(--blue)" stroke-width="1.5"/><rect x="9.5" y="6.5" width="7" height="13" rx="1.5" fill="none" stroke="var(--blue)" stroke-width="1.5"/><circle cx="13" cy="17" r=".9" fill="var(--blue)"/></svg>
        <div><p class="feat-title">Mobil nutzbar</p><p>TOLDA auch auf mobilen Geräten nutzen</p></div>
      </div>
      <div class="feat">
        <svg class="icon" viewBox="0 0 26 26" aria-hidden="true"><circle cx="13" cy="13" r="12" fill="#fff" stroke="var(--blue)" stroke-width="1.5"/><rect x="6" y="8" width="11" height="8" rx="1" fill="none" stroke="var(--blue)" stroke-width="1.5"/><rect x="15" y="11" width="5" height="8" rx="1" fill="#fff" stroke="var(--blue)" stroke-width="1.5"/></svg>
        <div><p class="feat-title">Einfach Daten synchronisieren</p><p>Aktuelle Daten in Textra Mail, auf dem Smartphone und weiteren Anwendungen</p></div>
      </div>
      <div class="feat">
        <svg class="icon" viewBox="0 0 26 26" aria-hidden="true"><circle cx="13" cy="13" r="12" fill="#fff" stroke="var(--blue)" stroke-width="1.5"/><ellipse cx="13" cy="8.5" rx="5" ry="2" fill="none" stroke="var(--blue)" stroke-width="1.4"/><path d="M8 8.5v9c0 1.1 2.2 2 5 2s5-.9 5-2v-9M8 13c0 1.1 2.2 2 5 2s5-.9 5-2" fill="none" stroke="var(--blue)" stroke-width="1.4"/></svg>
        <div><p class="feat-title">Leistungsstarke Datenbank</p><p>Gleichzeitig mit beliebig vielen Usern arbeiten (Kernel SQL)</p></div>
      </div>
      <div class="feat">
        <svg class="icon" viewBox="0 0 26 26" aria-hidden="true"><circle cx="13" cy="13" r="12" fill="#fff" stroke="var(--blue)" stroke-width="1.5"/><circle cx="9" cy="11" r="2" fill="none" stroke="var(--blue)" stroke-width="1.3"/><circle cx="13" cy="10" r="2" fill="none" stroke="var(--blue)" stroke-width="1.3"/><circle cx="17" cy="11" r="2" fill="none" stroke="var(--blue)" stroke-width="1.3"/><path d="M6 18c0-3 6-3 7-3s7 0 7 3" fill="none" stroke="var(--blue)" stroke-width="1.3"/></svg>
        <div><p class="feat-title">Mandantenfähig</p><p>Arbeiten Sie mit beliebig vielen Mandanten</p></div>
      </div>
    </div>

    <div class="abs features feat-col-b">
      <div class="feat">
        <svg class="icon" viewBox="0 0 26 26" aria-hidden="true"><circle cx="13" cy="13" r="12" fill="#fff" stroke="var(--blue)" stroke-width="1.5"/><circle cx="13" cy="13" r="5" fill="none" stroke="var(--blue)" stroke-width="3" stroke-dasharray="2.2 1.7"/><circle cx="13" cy="13" r="2" fill="var(--blue)"/></svg>
        <div><p class="feat-title">Flexible Berechtigungssteuerung</p><p>Global und mandantenbezogene Einstellungen möglich</p></div>
      </div>
      <div class="feat">
        <svg class="icon" viewBox="0 0 26 26" aria-hidden="true"><circle cx="13" cy="13" r="12" fill="#fff" stroke="var(--blue)" stroke-width="1.5"/><path d="M8 12a5 5 0 0 1 9-2M18 14a5 5 0 0 1-9 2" fill="none" stroke="var(--blue)" stroke-width="1.4"/><path d="M17 7v3h-3M9 19v-3h3" fill="none" stroke="var(--blue)" stroke-width="1.4"/></svg>
        <div><p class="feat-title">Integriertes Archiv</p><p>Automatisierte Ablage von E-Mails und Dokumenten</p></div>
      </div>
      <div class="feat">
        <svg class="icon" viewBox="0 0 26 26" aria-hidden="true"><circle cx="13" cy="13" r="12" fill="#fff" stroke="var(--blue)" stroke-width="1.5"/><rect x="7" y="11" width="7" height="4" rx="2" transform="rotate(-45 10.5 13)" fill="none" stroke="var(--blue)" stroke-width="1.5"/><rect x="12" y="11" width="7" height="4" rx="2" transform="rotate(-45 15.5 13)" fill="none" stroke="var(--blue)" stroke-width="1.5"/></svg>
        <div>
          <p class="feat-title">Umfangreiche Schnittstellen</p>
          <ul class="ticks feat-list">
            <li>BAUDAT</li>
            <li>Online-Projektraum</li>
            <li>ImmoLink (registrierte/r ImmoLink Nutzer/In)</li>
            <li>Textra Write</li>
            <li>Textra Calc</li>
            <li>Textra Mail</li>
            <li>Folio Reader (PDF)</li>
            <li>Finanzbuchhaltungen wie FINDAT, Addera, Lexiro etc.</li>
            <li>DMS-System (Dokumentenmanagementsystem ARKO)</li>
          </ul>
        </div>
      </div>
    </div>

    <div class="abs photo-team" role="img" aria-label="Foto: Besprechung am Tisch mit Bauplänen, Tablet und Bauhelm"></div>
    <div class="abs service">
      <h3 class="service-title">Unser Service für Sie</h3>
      <ul class="ticks">
        <li>Schulungen – online und vor Ort</li>
        <li>IT-System Service</li>
        <li>Projektmanagement</li>
        <li>Software Entwicklung</li>
        <li>Beratung Geschäftsprozessoptimierung und IT Ausstattung</li>
        <li>uvm.</li>
      </ul>
    </div>

    <p class="abs footer-url">www.bautraeger-werkbank.de</p>
    <p class="abs page-no">02</p>
  </section>

</main>
</body>
</html>
```